Brightfield Parking Lot Vision Flags

Size: 3 banners - 2' x 4' banners (portrait)
Design: all the same design with different text
text on banner 1: Building Solid Lives
text on banner 2: Come. Hear. Do. Luke 6
text on banner 3: Worship Center
Details: Use the colors red, white and black and use the r logo attached
Make white the main color (not too much black and not too much red) Keep design simple - not a lot of different textures - more "plumb like"

Target Market(s)

30-50 year olds

Industry/Entity Type

Parking

Font styles to use
Sans Serif

Colors
ec1f27
fbfbfb
1b1b1b

Requirements
Must have
• Logo and the colors red white and black
Nice to have
• simple - clean - cool
Should not have
• busy backgrounds and textures

```html
<!DOCTYPE html>
<html lang="en">
<head>
<meta charset="utf-8">
<title>Brightfield – Worship Center Flag</title>
<link rel="stylesheet" href="https://fonts.googleapis.com/css2?family=Inter:wght@700&display=swap">
<style>
  :root {
    --backdrop: #d1d2d4;
    --flag-white: #ffffff;
    --flag-fade: #e6e7e8;
    --brand-red: #ec1f27;
    --swoosh-red: #ef3340;
    --ink: #000000;
  }
  html, body {
    margin: 0;
    padding: 0;
    width: 1200px;
    height: 1200px;
    overflow: hidden;
    background: var(--backdrop);
  }
  .canvas {
    position: relative;
    width: 1200px;
    height: 1200px;
    background: var(--backdrop);
  }
  .flag {
    position: absolute;
    left: 300px;
    top: 0;
    width: 600px;
    height: 1200px;
    background: linear-gradient(to bottom,
      var(--flag-white) 0%,
      var(--flag-white) 73%,
      #f4f4f4 88%,
      var(--flag-fade) 100%);
    font-family: "Inter", "Helvetica Neue", Arial, sans-serif;
    font-weight: 700;
  }
  .brand-name {
    position: absolute;
    left: 0;
    width: 100%;
    top: 158px;
    margin: 0;
    text-align: center;
    font-size: 40px;
    line-height: 48px;
    letter-spacing: -0.5px;
    color: var(--brand-red);
  }
  .headline {
    margin: 0;
  }
  .headline-line {
    position: absolute;
    left: 0;
    width: 100%;
    text-align: center;
    font-size: 124px;
    line-height: 124px;
    letter-spacing: -2px;
    color: var(--ink);
  }
  .headline-line--top { top: 451px; }
  .headline-line--bottom { top: 627px; }
  .swoosh {
    position: absolute;
    left: 140px;
    top: 580px;
    width: 320px;
    height: 44px;
  }
</style>
</head>
<body>
  <div class="canvas">
    <section class="flag">
      <p class="brand-name">Brightfield</p>
      <h1 class="headline">
        <span class="headline-line headline-line--top">Worship</span>
        <span class="headline-line headline-line--bottom">Center</span>
      </h1>
      <svg class="swoosh" viewBox="0 0 320 44" aria-hidden="true">
        <path d="M2 38 C 90 14, 230 -2, 318 26 L 314 28 C 230 4, 95 18, 2 38 Z" fill="var(--swoosh-red)"/>
      </svg>
    </section>
  </div>
</body>
</html>
```